Kelvora

I ran out of business cards I designed myself on line. THe company went out of business and I LOVE my card. I am hoping someone can recreate the look or something equally as appealing to me.

Industry/Entity Type

Business

Colors
ecdaeb
f7f1f7

Requirements
Must have
• The card is going to be printed by a company Taroq.com. they are very high end stock and I market to high end clients…the logo needs to remain small and centered at the top. If it helps my web site is kelvora.net you can see there how I left the logo very small

```html
<!DOCTYPE html>
<html lang="en">
<head>
<meta charset="utf-8">
<title>Kelvora Business Card</title>
<link rel="stylesheet" href="https://fonts.googleapis.com/css2?family=Crimson+Text:wght@400&display=swap">
<style>
  :root {
    --page-bg: #ffffff;
    --card-bg: #fbfbe2;
    --card-border: #9178b4;
    --ink: #6a2b14;
    --ornament-main: #8a4a2c;
    --ornament-soft: #c9a58c;
  }
  * { margin: 0; padding: 0; box-sizing: border-box; }
  html, body {
    width: 693px;
    height: 1200px;
    overflow: hidden;
    background: var(--page-bg);
  }
  .canvas {
    position: relative;
    width: 693px;
    height: 1200px;
  }
  .business-card {
    position: absolute;
    left: 247px;
    top: 0;
    width: 213px;
    height: 383px;
    background: var(--card-bg);
    border: 4.5px solid var(--card-border);
    font-family: "Crimson Text", Georgia, serif;
    color: var(--ink);
    text-align: center;
    text-transform: uppercase;
  }
  .crest {
    position: absolute;
    left: 50px;
    top: 16px;
    width: 104px;
    height: 138px;
    border-radius: 40% 40% 45% 45%;
    background: radial-gradient(ellipse at center, var(--ornament-soft) 0%, var(--ornament-main) 75%, transparent 76%);
    opacity: 0.55;
  }
  .card-line {
    position: absolute;
    left: 0;
    right: 0;
    font-size: 14.5px;
    line-height: 1;
    letter-spacing: 0.2px;
    white-space: nowrap;
  }
  .company-name { top: 188px; }
  .services { top: 242px; }
  .person-name { top: 296px; }
  .phone { top: 321px; font-size: 14px; }
  .email { top: 338px; }
</style>
</head>
<body>
  <div class="canvas">
    <section class="business-card">
      <div class="crest" role="img" aria-label="Ornamental heart-shaped crest with scrolling vines"></div>
      <p class="card-line company-name">Kelvora, LLC</p>
      <p class="card-line services">Design &amp; Renovation</p>
      <p class="card-line person-name">Marisol Venderet</p>
      <p class="card-line phone">410-555-0187</p>
      <p class="card-line email">marisol@kelvora.net</p>
    </section>
  </div>
</body>
</html>
```